"Quiet Meadow" Organic Grocery Retail Packaging

"Quiet Meadow" is retail brand for Indian organic food products in following categories
- Lentils (2 lb and 4 lb)
- Flours (2 lb and 4 lb)
- Spices (whole spices like Cumin seeds) (100 gms, 200 gms, 400 gms)
- Spice Powders (Powdered spices like Chili powder) (100 gms, 200 gms, 400 gms)
- Masala Mixes (spices mixed together such as Garam Masala) (100 gms, 200 gms, 400 gms)
- Flour (10 lb - No transparent front part in this)

We are looking for one package design (except 10 lb flour) that will work for all categories, differentiated by at least color.
- Reference for competitors: 31Kavelo.com

Industry/Entity Type

Grocery Store

Requirements
Must have
• - Package design must have transparent part in front to show product inside
• - Front and back design
• - KPTR Organic logo and Non GMO logo
• - Back - Bar code, Nutrition Facts etc.
Nice to have
• We have an old logo in the attached CDR file. It would be nice to have a newer/updated logo.

```html
<!DOCTYPE html>
<html lang="en">
<head>
<meta charset="utf-8">
<title>Quiet Meadow – Cumin Seeds Pouch</title>
<link rel="stylesheet" href="https://fonts.googleapis.com/css2?family=Kaushan+Script&family=Oswald:wght@600&display=swap">
<style>
  :root {
    --backdrop: #ddd6d0;
    --kraft: #dcc3a0;
    --kraft-deep: #cfae85;
    --window: #e6d6bf;
    --window-light: #efe4d3;
    --ink: #3d2e22;
    --band: #5a4632;
    --band-deep: #3f3023;
    --cream: #efdcb8;
    --seed: #9c8873;
    --seed-deep: #6f5d4c;
    --badge-green: #1e8a5a;
    --white: #ffffff;
    --weight-grey: #cfc7bd;
  }
  html, body {
    margin: 0;
    padding: 0;
    width: 1200px;
    height: 1111px;
    overflow: hidden;
    background: var(--backdrop);
  }
  .canvas {
    position: relative;
    width: 1200px;
    height: 1111px;
  }
  .pouch-art {
    position: absolute;
    left: 0;
    top: 0;
  }
  .brand-name {
    position: absolute;
    left: 470px;
    top: 322px;
    width: 220px;
    text-align: center;
    font-family: "Kaushan Script", cursive;
    font-size: 40px;
    line-height: 1;
    color: var(--ink);
    margin: 0;
  }
  .product-name {
    position: absolute;
    left: 505px;
    top: 470px;
    font-family: "Kaushan Script", cursive;
    font-size: 98px;
    line-height: 1;
    color: var(--ink);
    margin: 0;
    transform: rotate(-4deg);
    transform-origin: left center;
  }
  .product-type {
    position: absolute;
    left: 648px;
    top: 578px;
    font-family: "Kaushan Script", cursive;
    font-size: 44px;
    line-height: 1;
    color: var(--cream);
    margin: 0;
    transform: rotate(-12deg);
  }
  .net-weight {
    position: absolute;
    left: 398px;
    top: 864px;
    font-family: "Oswald", sans-serif;
    font-weight: 600;
    font-size: 28px;
    letter-spacing: 1px;
    color: var(--weight-grey);
    margin: 0;
  }
</style>
</head>
<body>
<main class="canvas">
  <svg class="pouch-art" width="1200" height="1111" viewBox="0 0 1200 1111" aria-hidden="false">
    <!-- pouch body -->
    <path class="pouch-body" d="M342 173 H838 Q846 173 846 181 V900 Q846 935 810 937 Q590 948 370 937 Q334 935 334 900 V181 Q334 173 342 173 Z" fill="var(--kraft)"/>
    <rect class="pouch-side-tone" x="780" y="245" width="66" height="640" fill="var(--kraft-deep)" opacity="0.45"/>
    <!-- hang hole -->
    <rect class="hang-hole" x="548" y="202" width="99" height="21" rx="8" fill="var(--white)"/>
    <!-- transparent window -->
    <rect class="window" x="370" y="245" width="439" height="632" rx="28" fill="var(--window)"/>
    <path class="window-highlight" d="M434 245 H690 Q712 320 690 390 Q640 470 520 470 Q420 450 434 245 Z" fill="var(--window-light)"/>
    <!-- non-GMO badge as plain shape -->
    <circle class="non-gmo-badge" cx="440" cy="552" r="34" fill="none" stroke="var(--ink)" stroke-width="5"/>
    <!-- brush stroke behind subtitle -->
    <rect class="subtitle-band" x="622" y="570" width="150" height="68" rx="6" fill="var(--band-deep)" transform="rotate(-10 697 604)"/>
    <!-- product photo area -->
    <path role="img" aria-label="Photo of whole cumin seeds seen through the pouch window" class="product-window"
      d="M374 720 Q380 668 450 664 Q590 662 640 740 Q670 800 640 873 H374 Z" fill="var(--seed)"/>
    <!-- bottom band -->
    <path class="bottom-band" d="M334 837 Q440 880 600 870 Q760 860 846 830 V900 Q846 935 810 937 Q590 948 370 937 Q334 935 334 900 Z" fill="var(--band)"/>
    <!-- organic certificate badge as plain shape -->
    <ellipse class="organic-badge" cx="733" cy="857" rx="52" ry="36" fill="var(--white)" stroke="var(--badge-green)" stroke-width="6"/>
  </svg>

  <p class="brand-name">Quiet Meadow</p>
  <h1 class="product-name">Cumin</h1>
  <p class="product-type">Seeds</p>
  <p class="net-weight">200 g</p>
</main>
</body>
</html>
```